AMAZING BLACK FRIDAY AD FOR PRINT OR THE WEB

Create a Black Friday ad for nitrile gloves. We are offering a box of 100, no-powder, exam grade nitrile gloves, for $9.99. No limit. Each case is $99. Create something simple, eye catching, cool. KestrelWrap.com. Sale ends on December 4th. While supplies last. We are a local medical supply company in Hawaii that serves the general public in addition to local businesses, government, etc. Gloves are in short supply and we have tons of inventory ready to sell.

Target Market(s)

Businesses that use supplies such as gloves

Industry/Entity Type

medical supplies

Requirements
Must have
• logo and website

```html
<!DOCTYPE html>
<html lang="en">
<head>
<meta charset="utf-8">
<title>Black Friday Sale – Nitrile Gloves</title>
<link rel="stylesheet" href="https://fonts.googleapis.com/css2?family=Anton&family=Kaushan+Script&family=Montserrat:wght@400;500;600;700;800;900&display=swap">
<style>
  :root {
    --bg: #000000;
    --green: #0a9444;
    --red: #ff1a1a;
    --white: #ffffff;
    --grey-dark: #4a4a4a;
    --grey-mid: #7a7a7a;
    --grey-text: #bdbdbd;
    --dot: #151515;
    --glove-light: #7cc4f2;
    --glove-dark: #3f93d6;
  }
  html, body {
    margin: 0;
    padding: 0;
    width: 1200px;
    height: 1200px;
    overflow: hidden;
    background: var(--bg);
  }
  .ad {
    position: relative;
    width: 1200px;
    height: 1200px;
    background: var(--bg);
    overflow: hidden;
    font-family: "Montserrat", Arial, sans-serif;
  }
  .dot-field {
    position: absolute;
    background: var(--dot);
    border-radius: 6px;
  }
  .headline {
    position: absolute;
    left: 100px;
    margin: 0;
    font-family: "Anton", "Oswald", sans-serif;
    font-weight: 400;
    color: var(--green);
    line-height: 1;
    letter-spacing: 1px;
    text-transform: uppercase;
    white-space: nowrap;
  }
  .headline--black { top: 45px; font-size: 208px; }
  .headline--friday { top: 267px; font-size: 208px; }
  .sale-script {
    position: absolute;
    left: 128px;
    top: 455px;
    margin: 0;
    font-family: "Kaushan Script", cursive;
    font-size: 200px;
    line-height: 1;
    color: var(--red);
    transform: rotate(-6deg);
    transform-origin: left center;
  }
  .deadline {
    position: absolute;
    left: 94px;
    top: 660px;
    width: 490px;
  }
  .deadline__lead,
  .deadline__date {
    margin: 0;
    font-weight: 900;
    font-size: 60px;
    line-height: 1;
    letter-spacing: -0.5px;
    text-transform: uppercase;
    white-space: nowrap;
  }
  .deadline__lead { color: var(--grey-dark); }
  .deadline__date { color: var(--green); margin-top: 6px; }
  .deadline__date sup { font-size: 32px; vertical-align: 26px; }
  .deadline__note {
    margin: 8px 0 0;
    font-weight: 400;
    font-size: 30px;
    color: var(--grey-mid);
    text-transform: uppercase;
    letter-spacing: 0.5px;
  }
  .deadline__rule {
    height: 4px;
    background: var(--green);
    margin-top: 10px;
  }
  .about {
    position: absolute;
    left: 96px;
    top: 852px;
    margin: 0;
    font-weight: 600;
    font-size: 17.5px;
    line-height: 27px;
    color: var(--grey-text);
    white-space: nowrap;
  }
  .brand {
    position: absolute;
    left: 96px;
    top: 978px;
    width: 316px;
    height: 176px;
    background: #050505;
    display: flex;
    align-items: flex-end;
    justify-content: center;
    padding-bottom: 34px;
    box-sizing: border-box;
  }
  .brand__name {
    font-weight: 800;
    font-size: 36px;
    color: var(--grey-mid);
    letter-spacing: -1px;
  }
  .product-photo {
    position: absolute;
    left: 604px;
    top: 40px;
    width: 496px;
    height: 380px;
    border-radius: 46% 40% 30% 48%;
    background: radial-gradient(ellipse at 55% 45%, var(--glove-light), var(--glove-dark) 80%);
    z-index: 2;
  }
  .offer {
    position: absolute;
    left: 680px;
    top: 432px;
    width: 406px;
    height: 708px;
    background: var(--green);
    border-radius: 30px 30px 46px 46px;
    z-index: 1;
    color: var(--white);
  }
  .offer__title {
    position: absolute;
    left: 52px;
    top: 80px;
    margin: 0;
    font-weight: 900;
    font-size: 68px;
    line-height: 60px;
    color: #000;
    text-transform: uppercase;
    letter-spacing: -0.5px;
  }
  .offer__rule {
    position: absolute;
    left: 52px;
    width: 296px;
    height: 3px;
    background: var(--white);
  }
  .offer__box {
    position: absolute;
    left: 52px;
    top: 242px;
    margin: 0;
    font-weight: 800;
    font-size: 28px;
    line-height: 30px;
    text-transform: uppercase;
  }
  .feature {
    position: absolute;
    left: 52px;
    display: flex;
    align-items: center;
    gap: 18px;
    font-weight: 700;
    font-size: 24px;
    line-height: 26px;
  }
  .feature svg { flex: none; }
  .price {
    position: absolute;
    left: 52px;
    top: 485px;
    display: flex;
    align-items: center;
    gap: 12px;
  }
  .price__amount {
    font-weight: 900;
    font-size: 86px;
    line-height: 1;
    letter-spacing: -2px;
  }
  .price__amount sup { font-size: 40px; vertical-align: 34px; }
  .price__note {
    font-weight: 500;
    font-size: 27px;
    line-height: 27px;
    text-transform: uppercase;
  }
  .case {
    position: absolute;
    left: 52px;
    top: 585px;
    display: flex;
    align-items: center;
    gap: 16px;
  }
  .case__label {
    font-weight: 900;
    font-size: 38px;
    line-height: 38px;
    text-transform: uppercase;
  }
  .case__amount {
    font-weight: 900;
    font-size: 96px;
    line-height: 1;
  }
  .case__amount sup { font-size: 44px; vertical-align: 40px; }
</style>
</head>
<body>
<main class="ad">
  <div class="dot-field" role="img" aria-label="Dot grid decoration" style="left:655px;top:120px;width:112px;height:42px;"></div>
  <div class="dot-field" role="img" aria-label="Dot grid decoration" style="left:1108px;top:72px;width:40px;height:106px;"></div>
  <div class="dot-field" role="img" aria-label="Dot grid decoration" style="left:456px;top:1014px;width:112px;height:44px;"></div>
  <div class="dot-field" role="img" aria-label="Dot grid decoration" style="left:530px;top:1076px;width:112px;height:44px;"></div>

  <h1 class="headline headline--black">Black</h1>
  <h1 class="headline headline--friday">Friday</h1>
  <p class="sale-script">Sale</p>

  <section class="deadline">
    <p class="deadline__lead">Sale ends on</p>
    <p class="deadline__date">December 4<sup>th</sup></p>
    <p class="deadline__note">Till supplies last</p>
    <div class="deadline__rule"></div>
  </section>

  <p class="about">We are a local medical supply company in Hawaii<br>that serves the general public in addition to local<br>businesses, government, etc. Gloves are in short<br>supply and we have tons of inventory ready to sell.</p>

  <div class="brand">
    <span class="brand__name">kestrelwrap.com</span>
  </div>

  <div class="product-photo" role="img" aria-label="Photo of a pair of blue nitrile exam gloves"></div>

  <section class="offer">
    <h2 class="offer__title">Nitrile<br>Gloves</h2>
    <div class="offer__rule" style="top:226px;"></div>
    <p class="offer__box">We are offering<br>a box of 100</p>
    <div class="offer__rule" style="top:317px;"></div>

    <div class="feature" style="top:338px;">
      <svg width="48" height="48" viewBox="0 0 48 48" aria-hidden="true">
        <circle cx="24" cy="24" r="21" fill="none" stroke="#000" stroke-width="3"/>
        <rect x="17" y="16" width="12" height="16" rx="2" fill="none" stroke="#000" stroke-width="2.5" transform="rotate(-30 24 24)"/>
        <line x1="10" y1="10" x2="38" y2="38" stroke="#000" stroke-width="3"/>
      </svg>
      <span>No-powder</span>
    </div>
    <div class="feature" style="top:402px;">
      <svg width="48" height="48" viewBox="0 0 48 48" aria-hidden="true">
        <circle cx="24" cy="24" r="21" fill="none" stroke="#000" stroke-width="3"/>
        <rect x="15" y="13" width="15" height="20" rx="2" fill="none" stroke="#000" stroke-width="2.5"/>
        <line x1="19" y1="19" x2="26" y2="19" stroke="#000" stroke-width="2"/>
        <line x1="19" y1="24" x2="24" y2="24" stroke="#000" stroke-width="2"/>
        <circle cx="30" cy="31" r="5" fill="var(--green)" stroke="#000" stroke-width="2"/>
        <polyline points="27.5,31 29.5,33 32.5,29" fill="none" stroke="#000" stroke-width="1.8"/>
      </svg>
      <span>Exam grade<br>nitrile gloves</span>
    </div>
    <div class="offer__rule" style="top:469px;"></div>

    <div class="price">
      <span class="price__amount"><sup>$</sup>9.99</span>
      <span class="price__note">No<br>limit</span>
    </div>
    <div class="offer__rule" style="top:570px;"></div>

    <div class="case">
      <span class="case__label">Each<br>case</span>
      <span class="case__amount"><sup>$</sup>99</span>
    </div>
  </section>
</main>
</body>
</html>
```